Quorvin Upcoming Gigs

One page graphic with my upcoming dates. Logo and photo attached, and sample from last flyer. Text:

QUORVIN

UPCOMING DATES

3/26/18 Tidal Plums (Las Vegas, NV)

4/1/18 Venture Hollow 2847 M St (Sac, CA)

4/8/18 Amber Heron (Sac, CA)

5/5/18 Low Ceiling @ Silver Moth (Sac, CA)

5/10/18 Pellman Art Museum (Sac, CA)

5/11/18 Vif Brume @ Cafe du Lierre (Sac, CA)

5/27/18 Sonnlicht JTR @ Vox (Sac, CA)

Save The Date: 9/21/18 Lanterns Festival (Puerto Nuevo, MX)

plazabook.example/quorvin482

Target Market(s)

House/Electronic Music

Industry/Entity Type

Night Club

Font styles to use
Sans Serif

Colors

Designer to choose colors to be used in the design.

Requirements
Must have
• Quorvin logo or something that looks good instead. Prefer photo to be in but not necessary.
Nice to have

```html
<!DOCTYPE html>
<html lang="en">
<head>
<meta charset="utf-8">
<title>Quorvin — Upcoming Dates</title>
<link href="https://fonts.googleapis.com/css2?family=Comfortaa:wght@500;700&family=Questrial&display=swap" rel="stylesheet">
<style>
  :root {
    --paper: #ffffff;
    --night: #0d0a14;
    --night-mid: #1b1020;
    --neon-pink: #ff6f8f;
    --neon-pink-glow: rgba(255, 60, 110, 0.75);
    --neon-white: #f4f2ff;
    --neon-white-glow: rgba(190, 200, 255, 0.7);
    --social-dot: #3b5bd6;
    --ink: #ffffff;
    --date-font: "Comfortaa", sans-serif;
    --text-font: "Questrial", sans-serif;
  }
  * { margin: 0; padding: 0; box-sizing: border-box; }
  html, body {
    width: 841px; height: 1200px; overflow: hidden;
    background: var(--paper);
  }
  .poster {
    position: absolute;
    left: 19px; top: 19px; width: 803px; height: 1163px;
    overflow: hidden;
    background: var(--night);
  }
  .crowd-backdrop {
    position: absolute; inset: 0;
    background:
      radial-gradient(ellipse 45% 30% at 12% 80%, rgba(212, 38, 28, 0.95), transparent 70%),
      radial-gradient(ellipse 50% 35% at 88% 82%, rgba(91, 42, 140, 0.9), transparent 75%),
      radial-gradient(ellipse 60% 25% at 50% 20%, rgba(138, 47, 106, 0.55), transparent 80%),
      radial-gradient(circle 50px at 75% 42%, rgba(90, 150, 180, 0.45), transparent 100%),
      linear-gradient(180deg, var(--night) 0%, var(--night-mid) 45%, #2a0f1e 70%, #1a0c22 100%);
  }
  .line {
    position: absolute; left: 0; width: 100%;
    text-align: center; line-height: 1;
    transform: translateY(-50%);
    white-space: nowrap;
  }
  .brand-name {
    font-family: var(--date-font);
    font-weight: 700;
    font-size: 100px;
    letter-spacing: 2px;
    color: var(--ink);
  }
  .section-heading {
    font-family: var(--date-font);
    font-weight: 500;
    font-size: 46px;
    letter-spacing: 3px;
    color: transparent;
    -webkit-text-stroke: 1.6px var(--neon-pink);
    text-shadow: 0 0 10px var(--neon-pink-glow), 0 0 3px var(--neon-pink-glow);
  }
  .gig-date {
    font-family: var(--date-font);
    font-weight: 700;
    font-size: 44px;
    color: transparent;
    -webkit-text-stroke: 1.5px var(--neon-white);
    text-shadow: 0 0 8px var(--neon-white-glow);
  }
  .festival-date { font-size: 52px; }
  .gig-venue {
    font-family: var(--text-font);
    font-size: 26px;
    color: var(--ink);
  }
  .festival-venue {
    font-family: var(--text-font);
    font-size: 32px;
    color: var(--ink);
  }
  .social-link {
    font-family: var(--text-font);
    font-size: 18px;
    color: var(--ink);
    display: flex; justify-content: center; align-items: center; gap: 8px;
  }
  .social-dot {
    width: 13px; height: 13px; border-radius: 50%;
    background: var(--social-dot);
  }
</style>
</head>
<body>
<main class="poster">
  <div class="crowd-backdrop" role="img" aria-label="Photo of a nightclub crowd with raised hands silhouetted against red and violet stage lights"></div>

  <h1 class="line brand-name" style="top:128px">QUORVIN</h1>
  <h2 class="line section-heading" style="top:232px">UPCOMING DATES</h2>

  <section class="gig-list">
    <p class="line gig-date" style="top:310px">3/26/18</p>
    <p class="line gig-venue" style="top:348px">Tidal Plums (Las Vegas, NV)</p>
    <p class="line gig-date" style="top:384px">4/1/18</p>
    <p class="line gig-venue" style="top:422px">Venture Hollow 2847 M St (Sac, CA)</p>
    <p class="line gig-date" style="top:458px">4/8/18</p>
    <p class="line gig-venue" style="top:496px">Amber Heron (Sac, CA)</p>
    <p class="line gig-date" style="top:532px">5/5/18</p>
    <p class="line gig-venue" style="top:570px">Low Ceiling @ Silver Moth (Sac, CA)</p>
    <p class="line gig-date" style="top:606px">5/10/18</p>
    <p class="line gig-venue" style="top:644px">Pellman Art Museum (Sac, CA)</p>
    <p class="line gig-date" style="top:680px">5/11/18</p>
    <p class="line gig-venue" style="top:718px">Vif Brume @ Cafe du Lierre (Sac, CA)</p>
    <p class="line gig-date" style="top:754px">5/27/18</p>
    <p class="line gig-venue" style="top:792px">Sonnlicht JTR @ Vox (Sac, CA)</p>
  </section>

  <section class="save-the-date">
    <h2 class="line section-heading" style="top:880px">SAVE THE DATE</h2>
    <p class="line gig-date festival-date" style="top:942px">9/21/18</p>
    <p class="line festival-venue" style="top:1000px">Lanterns Festival</p>
    <p class="line festival-venue" style="top:1040px">(Puerto Nuevo, MX)</p>
  </section>

  <p class="line social-link" style="top:1124px"><span class="social-dot"></span>plazabook.example/quorvin482</p>
</main>
</body>
</html>
```